依頼詳細
背景は白で、シンプルだけど、ひとひねりの意味のあるスタイリッシュで知的なデザインを希望しております。カラフルでは無く、モダンで未来的なニュアンスがあると尚良いです。

裏面は、事業内容を3つ掲載したいです。
裏面は、とにかくシンプルが良いです。

書体は明朝とゴシックのどちらの案も見てみたいです。

※会社ロゴを添付いたしますので、色調をなるべく合わせていただきたいです。
※サイトから会社の雰囲気を読み取っていただきたいです。
URL:http://brightlanexy.com/

紙は、厚みのある固めの高級紙を使用します。
記載項目
(表面)・会社ロゴ ・名前:佐藤春樹  ・ふりがな:(Sato Haruki)
・役職:マーケティングディレクター ・ふりがな:(Marketing Director)
・電話番号:029-481-7263
・メール全体:info@brightlanexy.com
・メール個人:h.sato@brightlanexy.com
・URL:http://brightlanexy.com/
・住所:〒310-0844 茨城県水戸市住吉町4-208-2
(裏面)・事業内容のみ▶︎ ウェブ制作 ウェブ広告運用 ECコンサルタント
希望イメージ
シンプル 複雑
単色 カラフル
暗い 明るい
日常 高級
遊び心 厳粛
未来的 伝統的
女性的 男性的
希望する色
青系

全体的に、シンプルだけど品があってかっこいいです。

ただのシンプルとは違い、遊び心が上手く出ているのがとても良いです。

ちょっとした一つの文字の配置の仕方で大きく変わるものなのだなと感心いたしました。

皆さんこのたびはご協力いただきまして誠にありがとうございました。

```html
<!DOCTYPE html>
<html lang="ja">
<head>
<meta charset="utf-8">
<title>Brightlane XY 名刺デザイン</title>
<link rel="stylesheet" href="https://fonts.googleapis.com/css2?family=Noto+Sans+JP:wght@400;500;700&family=Roboto:wght@400;500;700&display=swap">
<style>
  :root {
    --board: #d7d8da;
    --paper: #ffffff;
    --brand-blue: #3b8dd4;
    --brand-blue-light: #5aa3e0;
    --navy: #1b3f7e;
    --ink: #222222;
    --muted: #6b6b6b;
    --logo-grey: #6f7276;
    --rule: #c9ccd0;
    --white: #ffffff;
  }
  * { margin: 0; padding: 0; box-sizing: border-box; }
  html, body { width: 805px; height: 1200px; overflow: hidden; }
  body {
    background: var(--board);
    font-family: "Noto Sans JP", "Roboto", sans-serif;
    color: var(--ink);
    position: relative;
  }
  .side-label {
    position: absolute;
    left: 40px;
    font-family: "Roboto", sans-serif;
    font-size: 20px;
    color: var(--muted);
  }
  .side-label--front { top: 68px; }
  .side-label--back { top: 626px; }

  .card {
    position: absolute;
    left: 40px;
    width: 725px;
    height: 450px;
    overflow: hidden;
    box-shadow: 0 1px 3px rgba(0,0,0,.15);
  }
  .card--front { top: 107px; background: var(--paper); }
  .card--back { top: 665px; background: var(--brand-blue); }

  /* front: upper */
  .tagline {
    position: absolute;
    left: 16px; top: 40px;
    padding-left: 18px;
    border-left: 6px solid var(--navy);
    font-size: 20px;
    font-weight: 700;
    color: var(--navy);
    line-height: 1.6;
    white-space: nowrap;
  }
  .tagline-rule {
    position: absolute;
    left: 16px; top: 92px;
    width: 400px; height: 1px;
    background: var(--rule);
  }
  .logo {
    position: absolute;
    right: 22px; top: 26px;
    display: flex;
    align-items: flex-start;
    gap: 10px;
  }
  .logo-name {
    font-family: "Roboto", sans-serif;
    font-weight: 700;
    font-size: 30px;
    line-height: 1.22;
    color: var(--logo-grey);
    text-align: right;
    white-space: nowrap;
  }
  .logo-mark {
    width: 28px; height: 28px;
    border-radius: 50%;
    background: var(--brand-blue);
    margin-top: 5px;
  }
  .person { position: absolute; left: 78px; top: 118px; }
  .person-title { font-size: 12px; color: var(--ink); letter-spacing: .02em; white-space: nowrap; }
  .person-title span { font-family: "Roboto", sans-serif; margin-left: 8px; }
  .person-name {
    margin-top: 6px;
    font-size: 38px;
    font-weight: 500;
    letter-spacing: .06em;
    line-height: 1.2;
    white-space: nowrap;
  }
  .person-name small {
    font-family: "Roboto", sans-serif;
    font-size: 14px;
    font-weight: 400;
    letter-spacing: 0;
    margin-left: 10px;
    color: var(--muted);
  }
  .person-mail {
    margin-top: 6px;
    display: flex; align-items: center; gap: 8px;
    font-family: "Roboto", sans-serif;
    font-size: 16px;
    white-space: nowrap;
  }
  .icon-box {
    display: inline-flex; align-items: center; justify-content: center;
    flex: none;
    width: 20px; height: 20px;
    background: var(--brand-blue);
    border-radius: 2px;
  }

  /* front: band */
  .info-band {
    position: absolute;
    left: 0; right: 0; bottom: 0;
    height: 210px;
    background: var(--brand-blue);
    color: var(--white);
  }
  .company-jp {
    position: absolute;
    right: 48px; top: 34px;
    font-size: 20px;
    font-weight: 500;
    letter-spacing: .04em;
    white-space: nowrap;
  }
  .contact-row {
    position: absolute;
    right: 0; top: 74px;
    width: 520px;
    height: 40px;
    padding: 0 48px 0 20px;
    display: flex; justify-content: flex-end; align-items: center; gap: 8px;
    background: var(--brand-blue-light);
    font-size: 15px;
    white-space: nowrap;
  }
  .contact-row .icon-box { background: var(--white); }
  .contact-row .tel { margin-left: 14px; display: inline-flex; align-items: center; gap: 8px; }
  .band-rule {
    position: absolute;
    right: 48px; top: 126px;
    width: 330px; height: 1px;
    background: rgba(255,255,255,.7);
  }
  .site-url {
    position: absolute;
    right: 48px; top: 140px;
    font-family: "Roboto", sans-serif;
    font-size: 20px;
    font-weight: 500;
    white-space: nowrap;
  }

  /* back */
  .back-url {
    position: absolute;
    right: 46px; top: 28px;
    font-family: "Roboto", sans-serif;
    font-size: 20px;
    font-weight: 500;
    color: var(--white);
    white-space: nowrap;
  }
  .cycle { position: absolute; left: 0; top: 0; }
  .cycle-node { fill: var(--white); }
  .cycle-arc { fill: none; stroke: var(--white); stroke-width: 9; }
  .cycle-head { fill: var(--white); }
  .cycle-label {
    font-family: "Noto Sans JP", sans-serif;
    font-size: 12px;
    fill: var(--brand-blue);
    text-anchor: middle;
    font-weight: 500;
  }
  .cycle-core {
    font-family: "Noto Sans JP", sans-serif;
    font-size: 32px;
    font-weight: 700;
    fill: var(--white);
    text-anchor: middle;
    letter-spacing: 2px;
  }
</style>
</head>
<body>
  <p class="side-label side-label--front">Front</p>
  <section class="card card--front">
    <p class="tagline">企業戦略を支えるウェブ戦略のプロ集団</p>
    <div class="tagline-rule"></div>

    <div class="logo">
      <p class="logo-name">Brightlane XY<br>LLC.</p>
      <span class="logo-mark"></span>
    </div>

    <div class="person">
      <p class="person-title">マーケティングディレクター<span>Marketing Director</span></p>
      <p class="person-name">佐藤 春樹<small>Haruki Sato</small></p>
      <p class="person-mail">
        <span class="icon-box">
          <svg width="14" height="10" viewBox="0 0 14 10"><rect x="0.5" y="0.5" width="13" height="9" fill="none" stroke="#fff"/><path d="M0.5 0.5 L7 6 L13.5 0.5" fill="none" stroke="#fff"/></svg>
        </span>
        h.sato@brightlanexy.com
      </p>
    </div>

    <div class="info-band">
      <p class="company-jp">ブライトレーン合同会社</p>
      <div class="contact-row">
        <span class="icon-box">
          <svg width="12" height="12" viewBox="0 0 12 12"><path d="M1 1.5H11M1 4.5H11M6 4.5V11" stroke="#3b8dd4" stroke-width="1.6" fill="none"/></svg>
        </span>
        <span>〒310-0844 茨城県水戸市住吉町4-208-2</span>
        <span class="tel">
          <span class="icon-box">
            <svg width="12" height="12" viewBox="0 0 12 12"><path d="M2.5 1 L4.5 1 L5.2 3.6 L3.8 4.6 Q5 7.2 7.4 8.2 L8.4 6.8 L11 7.5 L11 9.5 Q11 11 9.5 11 Q1 10 1 2.5 Q1 1 2.5 1Z" fill="#3b8dd4"/></svg>
          </span>
          029-481-7263
        </span>
      </div>
      <div class="band-rule"></div>
      <p class="site-url">http://brightlanexy.com/</p>
    </div>
  </section>

  <p class="side-label side-label--back">Back</p>
  <section class="card card--back">
    <p class="back-url">http://brightlanexy.com/</p>
    <svg class="cycle" width="725" height="450" viewBox="0 0 725 450" aria-label="事業内容の好循環図">
      <path class="cycle-arc" d="M407 156 A95 95 0 0 1 457 243"/>
      <polygon class="cycle-head" points="455,260 445,240 467,240"/>
      <path class="cycle-arc" d="M412 321 A95 95 0 0 1 312 321"/>
      <polygon class="cycle-head" points="298,314 318,311 308,331"/>
      <path class="cycle-arc" d="M267 243 A95 95 0 0 1 317 156"/>
      <polygon class="cycle-head" points="331,148 322,166 311,147"/>

      <text class="cycle-core" x="362" y="252">好循環</text>

      <circle class="cycle-node" cx="350" cy="102" r="50"/>
      <text class="cycle-label" x="350" y="106">ウェブ制作</text>

      <circle class="cycle-node" cx="492" cy="322" r="50"/>
      <text class="cycle-label" x="492" y="317">EC</text>
      <text class="cycle-label" x="492" y="335">コンサルタント</text>

      <circle class="cycle-node" cx="230" cy="316" r="50"/>
      <text class="cycle-label" x="230" y="311">ウェブ</text>
      <text class="cycle-label" x="230" y="329">広告運用</text>
    </svg>
  </section>
</body>
</html>
```